Flyer/Poster design required for volunteer activities

We need a STRIKING A4 Poster/Flyer advertising our conservation volunteer program activities which are currently happening in the area. This poster is to advertise the program once people have arrived on the island or to locals. The program covers 5 months, May-September 2019 and is focused on conservation. I have attached the following:
- a flyer which was previously created (QMR Habitat Helpers 2019 sm)to advertise the program - would prefer it has a similar striking resemblance, but not essential
- A mock up document 'HHQMR On Island Poster_2019_v2' with text -Logos-Images

Target Market(s)

Everyone interested in Environmental Adventure/Hiking/Citizen Science

Industry/Entity Type

Tourism

Font styles to use
Sans Serif

Requirements
Must have
• -A travel conservation focus
• -Must use 'QMR-Background Image' as the background to the design
• -The info of where to get more information and the social media details must be prominent

```html
<!DOCTYPE html>
<html lang="en">
<head>
<meta charset="utf-8">
<title>QMR Habitat Helpers 2019</title>
<link rel="stylesheet" href="https://fonts.googleapis.com/css2?family=Bebas+Neue&family=Open+Sans:wght@400;700&display=swap">
<style>
:root{
  --blue:#1b56b8;
  --blue-dark:#123f8f;
  --navy:#0b1d3a;
  --yellow:#ffdb1a;
  --white:#ffffff;
  --ink:#111827;
}
*{box-sizing:border-box;margin:0;padding:0}
html,body{width:750px;height:1200px;overflow:hidden;background:#fff}
.flyer{position:relative;width:750px;height:1200px;overflow:hidden;font-family:"Open Sans",Arial,sans-serif;color:var(--white)}
.backdrop{position:absolute;inset:0;background:linear-gradient(180deg,#dff3fb 0%,#bfe4f4 14%,#5fb2dd 30%,#2a86c6 48%,#1d6aa2 62%,#1f4d54 78%,#0d1e2e 100%)}
.frame{position:absolute;left:28px;top:28px;right:28px;bottom:28px;border:8px solid var(--yellow)}
.logo{position:absolute;left:70px;top:60px;width:140px;height:140px;border-radius:50%;background:var(--white);border:5px solid var(--blue);display:flex;align-items:center;justify-content:center;font-family:"Bebas Neue",sans-serif;font-size:34px;color:var(--blue)}
.title{position:absolute;left:240px;top:55px;font-family:"Bebas Neue",sans-serif;line-height:.9}
.title .place{display:block;font-size:78px;color:var(--blue)}
.title .program{display:block;font-size:42px;color:var(--ink);margin-top:8px}
.dates{position:absolute;left:70px;top:262px;display:flex;align-items:stretch;font-family:"Bebas Neue",sans-serif}
.dates .season{background:var(--yellow);color:var(--ink);font-size:40px;padding:2px 22px 0}
.dates .tagline{background:var(--blue);color:var(--white);font-size:20px;padding:0 18px;display:flex;align-items:center}
.join{position:absolute;left:0;right:0;top:318px;text-align:center;font-family:"Bebas Neue",sans-serif;font-size:32px;color:var(--white);-webkit-text-stroke:1.2px var(--ink)}
.month{position:absolute;width:310px}
.month .head{position:relative;height:130px}
.photo{position:absolute;left:0;top:0;width:124px;height:124px;border-radius:50%;border:6px solid var(--yellow)}
.label{position:absolute;left:110px;top:6px;background:var(--yellow);color:var(--ink);font-family:"Bebas Neue",sans-serif;font-size:30px;padding:0 14px 0 16px;line-height:1.1;white-space:nowrap}
.week{position:absolute;left:128px;top:44px;background:var(--blue);font-family:"Bebas Neue",sans-serif;font-size:15px;line-height:1.05;padding:4px 10px;white-space:nowrap}
.theme{position:absolute;left:136px;top:88px;font-family:"Bebas Neue",sans-serif;font-size:16px;line-height:1;white-space:nowrap}
.list{list-style:none;font-size:11px;font-weight:700;line-height:1.38;margin-top:6px}
.list li{position:relative;padding-left:13px}
.list li::before{content:"";position:absolute;left:0;top:5px;width:7px;height:7px;border-radius:50%;background:var(--yellow)}
.may{left:70px;top:375px}
.june{left:390px;top:375px}
.july{left:70px;top:640px}
.august{left:390px;top:640px}
.september{left:70px;top:905px;width:610px;display:flex;gap:30px}
.september .head{width:300px;flex:none}
.september .list{margin-top:0;padding-top:4px}
.info{position:absolute;left:36px;right:36px;top:1086px;background:var(--blue);text-align:center;font-size:13px;font-weight:700;padding:8px 6px}
.follow{position:absolute;left:0;right:0;top:1128px;display:flex;justify-content:center;align-items:center;gap:12px;font-size:13px;font-weight:700;line-height:20px}
.dot{width:16px;height:16px;border-radius:3px;background:var(--yellow)}
.follow .gap{width:26px}
</style>
</head>
<body>
<main class="flyer">
  <div class="backdrop" role="img" aria-label="Aerial photograph of the island lagoon, turquoise reef water and forested mountain ridge"></div>
  <div class="frame"></div>

  <div class="logo">HHQMR</div>
  <h1 class="title"><span class="place">QUILLMERE<br>ISLAND</span><span class="program">HABITAT HELPERS</span></h1>

  <div class="dates"><span class="season">MAY-SEPTEMBER 2019</span><span class="tagline">BE INVOLVED IN PROTECTING PARADISE</span></div>
  <h2 class="join">JOIN THE QMR HABITAT HELPERS PROGRAM 2019</h2>

  <section class="month may">
    <div class="head">
      <div class="photo" role="img" aria-label="Photo of a seabird chick in nesting grass" style="background:linear-gradient(135deg,#7a8a5a,#c9b79a)"></div>
      <div class="label">MAY 2019</div>
      <div class="week">FEATURE WEEK:<br>19TH – 26TH MAY</div>
      <div class="theme">BIRDS OF<br>QUILLMERE ISLAND</div>
    </div>
    <ul class="list">
      <li>Ocean bird watching boat trips</li>
      <li>Guided tours of Woodhen and Currawong quarters</li>
      <li>Weekly lectures at the Quillmere Island Museum</li>
      <li>Weekly screenings of documentaries on Bird and Island Conservation projects</li>
      <li>Self guided land bird survey tours</li>
    </ul>
  </section>

  <section class="month june">
    <div class="head">
      <div class="photo" role="img" aria-label="Photo of a snorkeller recording marine data underwater" style="background:linear-gradient(135deg,#0e3c6e,#4aa0d8)"></div>
      <div class="label">JUNE 2019</div>
      <div class="week">FEATURE WEEK:<br>3RD – 9TH JUNE</div>
      <div class="theme">QUILLMERE ISLAND<br>MARINE PARK</div>
    </div>
    <ul class="list">
      <li>Marine pest monitoring with marine park staff</li>
      <li>Marine plastic &amp; debris clean up activities</li>
      <li>Screenings of marine conservation documentaries at the museum</li>
      <li>Weekly lectures on Marine Life at the Quillmere Island Museum</li>
      <li>Marine Activities with local operators</li>
    </ul>
  </section>

  <section class="month july">
    <div class="head">
      <div class="photo" role="img" aria-label="Photo of volunteers removing invasive weeds in the forest" style="background:linear-gradient(135deg,#3d5a2a,#a88a55)"></div>
      <div class="label">JULY 2019</div>
      <div class="week">FEATURE WEEK:<br>21ST – 28TH JULY</div>
      <div class="theme">INVASIVE<br>SPECIES</div>
    </div>
    <ul class="list">
      <li>Guided walks to learn about the weed eradication program</li>
      <li>Weekly lectures on plants of Quillmere Island</li>
      <li>Weekly screenings of documentaries on plant and island conservation projects</li>
      <li>Guided walks to Mount Ashby</li>
    </ul>
  </section>

  <section class="month august">
    <div class="head">
      <div class="photo" role="img" aria-label="Photo of a hiker on a coastal ridge above the sea" style="background:linear-gradient(180deg,#9fd0ee,#3f6f4a)"></div>
      <div class="label">AUGUST 2019</div>
      <div class="week">FEATURE WEEK:<br>11TH – 19TH AUGUST</div>
      <div class="theme">AMAZING<br>INVERTEBRATES</div>
    </div>
    <ul class="list">
      <li>Guided night walks to learn about the island's invertebrates</li>
      <li>Weekly viewing and presentation of the Quillmere Island Phasmid</li>
      <li>Weekly lectures on invertebrates of Quillmere Island at the museum</li>
      <li>Weekly screenings of documentaries on island conservation projects</li>
    </ul>
  </section>

  <section class="month september">
    <div class="head">
      <div class="photo" role="img" aria-label="Photo of a stick insect held in open hands" style="background:linear-gradient(135deg,#c99a84,#5a3e36)"></div>
      <div class="label">SEPTEMBER 2019</div>
      <div class="week">FEATURE WEEK:<br>1ST – 8TH SEPTEMBER</div>
      <div class="theme">PROTECTING<br>PARADISE</div>
    </div>
    <ul class="list">
      <li>Observational snorkel surveys with Marine Ecologists, to assess populations of Ashby Anemonefish and other unique fish species</li>
      <li>Guided snorkel and glass bottom boat tour to assess coral health within the Quillmere Island Marine Park</li>
      <li>Guided walks to learn about the island's conservation history</li>
    </ul>
  </section>

  <p class="info">See the QMR visitor centre for more information about the QMR Habitat Helpers program for 2019</p>
  <div class="follow">
    <span>FOLLOW US!</span>
    <span class="dot"></span><span>www.hhqmr-social.org</span>
    <span class="gap"></span>
    <span class="dot"></span><span>photos@hhqmr</span>
  </div>
</main>
</body>
</html>
```